Home Page Design for Motor Manufacturer

Hello,
please design the homepage for a manufacturer of industry motors. I am looking for a professional, clean and minimalistic design. Since this a rather conservative industry it should get a professional look but since it is a redesign there should be some modern that gives is the modern touch of innovation.
A competitor's homepage I like is:
https://www.valtrosk.com/en/
What I like about this website:
* clean, minimal, well structured design
* mega menu
For this project please find attached the wireframes (most buttons are in German but by context and Google translate you will easily figure it out; only unclear - "Messe" means "trade exhibition"). The paddings and margins are NOT exact. Also any color of backgrounds etc. chosen is not meant to represent a real color but rather to illustrate the object and maybe show there should be some background emphasis (color or image).
Wireframes:
https: //www.filmavek. com / t / pxuTQmD7ZJHaLrwY
In both wireframes the only thing that is different is the Service section. I expect from the winner both designs for this service section: one with normal cart design and one with tabs as filters to search products (find image for product categories attached)
In the header use on the left the following text:
h1: "Your competent partner for industrial engines,
-transmission and drawing parts
with more than 5000 satisfied customers "
primary button: Our products
sec. button: Download catalog
and on the right side we feature one or more product images (like putting them in a nice display together).
I also think of a solid background color or subtle gradient for the hero section.
The winner should also design an open mega menu version.
Menu items in this order:
• Home page
• Gearboxes & Motors
• Engine components
• Drawing parts
• Machines & accessories
• About us
• Contact
Also create a language switch with globe symbol and DE for Germany and EN for English above the nav plus the telephone number with icon (user dummy number +49 (0) 987654321)
Output should be in Figma, Sketch or PSD.
Fonts + color to use:
header: Proza Libre, bold, # 0171A1
body: Open Sans, regular, black
Primary accent color: # 0171A1
Text black or dark gray
background: light gray, white or shade of blue
More image resources:
https://www.filmavek.com/t/QrnLVdHZPKEX1bmu
If there are any questions please do not hesitate to ask.
Target Market(s)
B2B - anyone with industrial machinery needing small motors (not car engines)
Industry/Entity Type
Manufacturing
Number of Pages Required
1 page
Requirements
Must have
- see above
Nice to have
- see above
Should not have
- see above

```html
<!DOCTYPE html>
<html lang="en">
<head>
<meta charset="utf-8">
<title>Delvar – Industrial engines, transmission and drawing parts</title>
<link rel="stylesheet" href="https://fonts.googleapis.com/css2?family=Open+Sans:wght@400;600&family=Proza+Libre:wght@500;700&family=Roboto:ital,wght@0,400;0,500;0,700;1,400&display=swap">
<style>
  :root {
    --accent: #0171A1;
    --ink: #1a1a1a;
    --muted: #6b6f73;
    --bg-top: #f0f8f5;
    --bg-bottom: #d9eff9;
    --white: #ffffff;
    --fair-blue: #1897e0;
    --fair-red: #ec2d22;
    --ribbon-red: #e2061a;
    --partner-navy: #1f3a8a;
    --stand-grey: #9a9da1;
    --note-grey: #6e7276;
  }
  * { box-sizing: border-box; margin: 0; padding: 0; }
  html, body { width: 764px; height: 1200px; overflow: hidden; }
  body {
    position: relative;
    font-family: "Open Sans", sans-serif;
    color: var(--ink);
    background: linear-gradient(165deg, var(--bg-top) 0%, var(--bg-top) 40%, var(--bg-bottom) 100%);
  }
  .utility-bar {
    position: absolute; top: 31px; right: 75px;
    display: flex; gap: 18px; align-items: center;
    font-size: 7px; font-weight: 600; color: var(--muted);
  }
  .utility-bar span { display: flex; align-items: center; gap: 2px; }
  .brand {
    position: absolute; left: 76px; top: 48px;
    font-family: "Proza Libre", sans-serif; font-weight: 700;
    font-size: 19px; color: var(--accent); letter-spacing: -0.5px;
  }
  .main-nav {
    position: absolute; top: 49px; left: 168px;
    display: flex; gap: 11.5px; font-size: 9.6px;
  }
  .main-nav a { color: var(--ink); text-decoration: none; padding: 0 2px 5px; }
  .main-nav a.is-active { border-bottom: 1.5px solid var(--accent); }
  .hero-visual {
    position: absolute; left: 374px; top: 77px;
    width: 610px; height: 610px; border-radius: 50%;
    background: radial-gradient(circle at 45% 50%, #f7f8f8 0%, #dfe2e3 45%, #c9cdcf 70%, #eceeee 100%);
  }
  .hero-copy { position: absolute; left: 74px; top: 175px; }
  .hero-title {
    font-family: "Proza Libre", sans-serif; font-weight: 700;
    font-size: 26.5px; line-height: 34.5px; color: var(--accent);
    width: 340px;
  }
  .hero-sub { margin-top: 18px; margin-left: 1px; font-size: 12.5px; }
  .hero-sub strong { color: var(--accent); font-weight: 400; }
  .hero-actions { display: flex; gap: 27px; margin-top: 23px; margin-left: 1px; }
  .btn {
    height: 32px; display: flex; align-items: center; justify-content: center;
    font-size: 9.8px; text-decoration: none;
  }
  .btn-primary { width: 155px; background: var(--accent); color: var(--white); }
  .btn-secondary { width: 79px; border: 1.5px solid var(--accent); color: var(--accent); }
  .section-title {
    position: absolute; left: 76px; top: 745px;
    font-family: "Proza Libre", sans-serif; font-weight: 500;
    font-size: 19.5px; color: var(--accent); word-spacing: 3px;
  }

  /* exhibition cards */
  .exhibition {
    position: absolute; top: 794px; width: 266px; height: 186px;
    background: var(--white); overflow: hidden;
    font-family: "Roboto", sans-serif;
  }
  .exhibition-voltara { left: 76px; border: 1px solid #9fd0ef; }
  .exhibition-montrix { left: 423px; border: 1px solid #555; }
  .fair-name { position: absolute; left: 12px; top: 8px; font-weight: 500; }
  .exhibition-voltara .fair-name { font-size: 16px; color: var(--fair-blue); top: 9px; }
  .exhibition-montrix .fair-name { font-size: 10.5px; color: #111; top: 4px; left: 13px; font-weight: 700; }
  .fair-square { position: absolute; left: 13px; top: 18px; width: 34px; height: 30px; background: #2b2b2b; }
  .fair-note { position: absolute; left: 13px; width: 145px; font-size: 6px; line-height: 10.5px; }
  .exhibition-voltara .fair-note { color: var(--note-grey); }
  .exhibition-montrix .fair-note { color: #111; }
  .fair-note-de { top: 49px; }
  .fair-note-en { top: 81px; font-style: italic; }
  .partner-name {
    position: absolute; left: 165px; top: 11px;
    font-weight: 700; font-size: 17px; color: var(--partner-navy);
  }
  .exhibition-montrix .partner-name { left: 167px; }
  .stand-info {
    position: absolute; left: 165px; top: 43px;
    font-size: 16px; line-height: 21px;
  }
  .exhibition-voltara .stand-info { color: var(--stand-grey); }
  .exhibition-montrix .stand-info { color: #111; left: 166px; }
  .stand-info b { font-weight: 700; display: block; }
  .fair-band {
    position: absolute; left: 0; right: 0; top: 130px; bottom: 0;
    color: var(--white); font-weight: 500;
  }
  .exhibition-voltara .fair-band { background: var(--fair-blue); }
  .exhibition-montrix .fair-band { background: var(--fair-red); }
  .fair-dates { position: absolute; left: 12px; top: 16px; font-size: 11px; line-height: 14.5px; }
  .fair-url { position: absolute; right: 8px; bottom: 7px; font-size: 10px; }
  .visit-ribbon {
    position: absolute; right: 0; top: 120px; width: 129px; height: 20px;
    display: flex; align-items: center; justify-content: center;
    font-size: 9px; color: var(--white); white-space: nowrap;
  }
  .visit-ribbon i { margin-left: 3px; }
  .exhibition-voltara .visit-ribbon { background: var(--ribbon-red); }
  .exhibition-montrix .visit-ribbon { background: #111; width: 128px; }

  .contact-bar {
    position: absolute; left: 76px; top: 1067px; width: 614px; height: 48px;
    background: var(--accent); color: var(--white);
    display: flex; align-items: center;
  }
  .contact-title {
    font-family: "Open Sans", sans-serif; font-size: 19px;
    padding: 0 11px 0 14px; border-right: 1px solid var(--white); line-height: 34px;
  }
  .contact-item { display: flex; align-items: center; gap: 3px; font-size: 9.5px; }
  .contact-phone { margin-left: 46px; }
  .contact-mail { margin-left: 101px; }
  .to-top { margin-left: 34px; }
</style>
</head>
<body>
  <div class="utility-bar">
    <span>
      <svg width="9" height="9" viewBox="0 0 24 24"><path fill="#6b6f73" d="M6.6 10.8a15 15 0 0 0 6.6 6.6l2.2-2.2a1 1 0 0 1 1-.25 11.4 11.4 0 0 0 3.6.57 1 1 0 0 1 1 1V20a1 1 0 0 1-1 1A17 17 0 0 1 3 4a1 1 0 0 1 1-1h3.5a1 1 0 0 1 1 1c0 1.25.2 2.45.57 3.57a1 1 0 0 1-.25 1z"/></svg>
      +49 (0) 987654321
    </span>
    <span>
      <svg width="9" height="9" viewBox="0 0 24 24"><circle cx="12" cy="12" r="10" fill="none" stroke="#6b6f73" stroke-width="2.5"/><path d="M2 12h20M12 2c3 3 3 17 0 20M12 2c-3 3-3 17 0 20" fill="none" stroke="#6b6f73" stroke-width="2"/></svg>
      EN
      <svg width="6" height="4" viewBox="0 0 6 4"><path d="M0.5 0.5 3 3 5.5 0.5" fill="none" stroke="#6b6f73"/></svg>
    </span>
  </div>

  <div class="brand">Delvar</div>

  <nav class="main-nav">
    <a class="is-active" href="#">Home</a>
    <a href="#">Gearboxes &amp; Motors</a>
    <a href="#">Engine components</a>
    <a href="#">Drawing parts</a>
    <a href="#">Machines &amp; accessories</a>
    <a href="#">About</a>
    <a href="#">Contact</a>
  </nav>

  <div class="hero-visual" role="img" aria-label="Product photo of a silver planetary gearbox with three gears around a central bearing"></div>

  <section class="hero-copy">
    <h1 class="hero-title">Your competent partner for industrial engines, transmission and drawing parts</h1>
    <p class="hero-sub">with more than <strong>5000 satisfied customers</strong></p>
    <div class="hero-actions">
      <a class="btn btn-primary" href="#">Our products</a>
      <a class="btn btn-secondary" href="#">Get catalog</a>
    </div>
  </section>

  <h2 class="section-title">Upcoming exhibition</h2>

  <article class="exhibition exhibition-voltara">
    <div class="fair-name">voltara drives</div>
    <p class="fair-note fair-note-de">Die Voltara Drives ist Europas führende Fachmesse für elektrische Automatisierung.</p>
    <p class="fair-note fair-note-en">Voltara Drives is Europe's leading exhibition for electric automation.</p>
    <div class="partner-name">Delvar</div>
    <div class="stand-info">Delvar GmbH<b>Halle 1</b><b>Stand 249</b></div>
    <div class="fair-band">
      <div class="fair-dates">24. - 26. November 2020<br>Nürnberg</div>
      <div class="fair-url">expo.voltara.com</div>
    </div>
    <div class="visit-ribbon">Besuchen Sie uns! <i>Visit us!</i></div>
  </article>

  <article class="exhibition exhibition-montrix">
    <div class="fair-name">Montrix</div>
    <div class="fair-square"></div>
    <p class="fair-note fair-note-de">Internationale Fachmesse für Produktion- und Montageautomatisierung</p>
    <p class="fair-note fair-note-en">International Trade Fair for Automation in Production and Assembly</p>
    <div class="partner-name">Delvar</div>
    <div class="stand-info">Delvar GmbH<b>Halle 8</b><b>Stand 8314</b></div>
    <div class="fair-band">
      <div class="fair-dates">05. - 08. Oktober 2020<br>Stuttgart</div>
      <div class="fair-url">www.montrix-messe.de</div>
    </div>
    <div class="visit-ribbon">Besuchen Sie uns! <i>Visit us!</i></div>
  </article>

  <footer class="contact-bar">
    <div class="contact-title">Contact und Inquiry</div>
    <div class="contact-item contact-phone">
      <svg width="10" height="12" viewBox="0 0 24 24"><path fill="#fff" d="M6.6 10.8a15 15 0 0 0 6.6 6.6l2.2-2.2a1 1 0 0 1 1-.25 11.4 11.4 0 0 0 3.6.57 1 1 0 0 1 1 1V20a1 1 0 0 1-1 1A17 17 0 0 1 3 4a1 1 0 0 1 1-1h3.5a1 1 0 0 1 1 1c0 1.250.2 2.45.57 3.57a1 1 0 0 1-.25 1z"/></svg>
      +49 2131 4406 185
    </div>
    <div class="contact-item contact-mail">
      <svg width="12" height="9" viewBox="0 0 24 18"><rect width="24" height="18" rx="2" fill="#fff"/><path d="M1 1l11 9 11-9" fill="none" stroke="#0171A1" stroke-width="2"/></svg>
      info@delvar-online.de
    </div>
    <svg class="to-top" width="13" height="12" viewBox="0 0 13 12"><path d="M1 6 6.5 1 12 6M1 11 6.5 6 12 11" fill="none" stroke="#cfe3ee" stroke-width="1.8"/></svg>
  </footer>
</body>
</html>
```